Guarding Virginia Theft Charges
Guarding Virginia Theft Charges - Law
Creative Brief
Title: Guarding Virginia Theft Charges Authors: Owen T. Marsh and Philip R. Oakes Cover Size (front back and spine): (8.5" x 11" landscape orientation)
Law
People charged with property crimes such as shop lifting, larceny, embezzlement, destruction of property, robbery. ect.
This project is for the entire cover of a paperback book (front, spine and back cover) that is half sheet size (8.5" x 5.5"). The front cover must have the title and the authors' names Owen T. Marsh and Philip R. Oakes The authors will later add the barcode, publishers logo a photograph of the author and text on the back page so any design on the back must look good even if covered in text and bar codes ect. Attached is an example of previous submissions for other projects that we have done.
tomaskrevel tomaskrevel
Pwardell, please check private messages. Top right corner
pwardell pwardell
#77 to be more clear take book number #77 and replace the image with the picture from #59
#77 After intense discussion by all the various people involved in this project we would really like to see the picture from #59 swapped out with the image from #77. Basically, we love the grey and the font ect. from #77 but people like the image with the security camera from #59 better. Can you do that?
#68 can you put the author's names in the lower left corner on top of one another?
#70 Way to go! I like the color and text and picture for #70 but I like the title and author's names and their orientation for #61. Can you take the title bar and pin strip and title and author's names from #61 and put it on the design and color and picture of #70 with the title on the top?
Everyone. Some common critiques that I am sending out over and over again: 1) We are looking for a strong but conservative and professional font/layout for the title and authors' names. See the uploaded examples as good examples. 2) Images should not be cliche (handcuffs, gavels, jail bars) 3) Custom images created from stock photos are preferable over simply taking a rectangular image and plopping it down onto the front cover. Make a composite from several photos, cut out and image, do a full bleed image on the front cover, use filters and layers to make the stock photo unique. These are examples of things that set submission images apart. 4) Avoid images that are scary, sexy, or too intense. Masked burglars breaking into a house, burglars with guns, bullet holes or blood. ect. Our audience are the people who have been charged with these crimes and we want to reassure them that we can help rather than scare them...they are already scared. 5) Absolutely no text or bar codes or images on the back cover. Everything on the back cover must be such that I can add on the image and text layers on top without ruining the look of the back cover. 6) I prefer textures backgrounds over monochromatic backgrounds (see the three book covers that we uploaded as examples).
#54, #55, #56 Gun wielding masked burglars and slash marks and bullets holes are a bit too intense. Remember our audience are the people being arrested for these crimes.
#12 I like the font and layout of the text you chose and I like that you have a full bleed image on the cover rather than a rectangular stock photo inserted into the cover. I just don't see the connection between the image and the book title. Try a similar layout with some different images. I think if you could nail the image you would have a very strong submission.
#10 I know I made a comment about the leather texture in a comment on another submission you did. I like the texture you used on this draft much better. I think you image usage is some of the best we are seeing but the text font and layout is holding you back. Take a look at the book covers we uploaded for an idea of the fonts and layouts that we liked for our previous quillspark projects.
#30 - the background color is better that some of your other versions for this submission but we are not wild about the layout or style for the title and author. We tend to prefer a more conservative font/layout (see the three book examples we included with our bid). I know I said that we liked the leather texture for the background but something a little more subtle and more similar to leather bound book cover would be better.
#51 - I like that you have created an image from the stock photo rather than just plugging in a rectangular stock photo for the cover image. However, the colors are too bold and the I don't like the title font/design. Try altering the colors and title and please submit some other ideas.
#43 please remove all the text and photo and bar codes ect. from the back cover. Submission with anything other than background will not be selected. It would be a shame, since its a good submission otherwise.
#48 could you do a couple version of this. 1) Try making the title font a little bit smaller or less bolded. 2) Try a version with the picture on the upper half of the front cover (rather than on the lower half) and the title and authors bellow the picture. 3) Try a background cover other than green - this version currently looks too similar to our Narcotics Charge Response Guide.
Everyone, remember the back cover it to be blank. Please do not submit drafts with pictures or text on the back cover.
Everyone, try to stay away from the generic criminal law pics: gavels, handcuffs, jail bars. ect.
#42 I like the font and the pic but the color choice is a bit intense.
EVERYONE: Remember, that this design is for the front, spine and backcover just like in the examples we included with this project. We will NOT select any entry that does not include front and back cover.
#6 I like the book title font, color and justification. Good job on using multiple colors and fonts effectively and professionally.
#4, #5 the major difference between this stock image and the image in #20 (which we really liked)is that the image in #4 & #5 seems to be a young lady showing a good amount of thigh in a very mini skirt and the picture seems to have a slightly sexy under current and it is hard to tell what she is doing. We really don't want this be at all racy.
#10 - I really like the creativity of having the guy stealing our book. It adds a nice light hardheartedness to it that prevents it from being too dark. The biggest down side, is that we are trying to present an image of a very successful high profile law firm and this might be a little bit too much humor to match the "elite professional" image we try to foster. Improving the execution of the font, color choices, background and most importantly the use of this cleaver image may pop-up the level of professionalism of the design. An extremely well executed and professional design could compensate for the levity in the image and strike a lovely balance.

```html
<!DOCTYPE html>
<html lang="en">
<head>
<meta charset="UTF-8">
<title>Guarding Virginia Theft Charges – Cover Spread</title>
<link href="https://fonts.googleapis.com/css2?family=Cinzel:wght@500;700&family=Cormorant+Garamond:wght@500;600&display=swap" rel="stylesheet">
<style>
  :root {
    --page-bg: #ffffff;
    --leather: #7b5636;
    --leather-light: #8e6642;
    --leather-dark: #5e3f25;
    --spine-line: rgba(40, 24, 12, 0.35);
    --gold-light: #f3dc9c;
    --gold: #d8b262;
    --gold-dark: #9c7330;
    --ring: #3b2414;
    --ring-edge: #a07a45;
    --scene-sky: #b7c9c4;
    --scene-green: #4f6a2e;
    --scene-house: #c7b08a;
  }
  * { margin: 0; padding: 0; box-sizing: border-box; }
  html, body {
    width: 1200px; height: 646px; overflow: hidden;
    background: var(--page-bg);
  }
  .canvas { position: relative; width: 1200px; height: 646px; }
  .cover-spread {
    position: absolute; left: 210px; top: 15px;
    width: 780px; height: 616px;
    display: flex;
    background:
      radial-gradient(ellipse at 30% 25%, var(--leather-light) 0%, transparent 55%),
      radial-gradient(ellipse at 75% 80%, var(--leather-light) 0%, transparent 50%),
      radial-gradient(ellipse at 50% 50%, var(--leather) 0%, var(--leather-dark) 120%);
    box-shadow: 0 0 0 1px rgba(0,0,0,0.12);
  }
  .back-cover, .front-cover { position: relative; width: 390px; height: 100%; }
  .back-cover { border-right: 2px solid var(--spine-line); }
  .front-cover {
    border-left: 1px solid rgba(160, 120, 80, 0.25);
    display: flex; flex-direction: column; align-items: center;
  }
  .title {
    margin-top: 22px;
    font-family: 'Cinzel', serif;
    text-align: center; line-height: 0.92;
    background: linear-gradient(180deg, var(--gold-light) 0%, var(--gold) 45%, var(--gold-dark) 100%);
    -webkit-background-clip: text; background-clip: text;
    color: transparent;
    filter: drop-shadow(1px 2px 1px rgba(30, 15, 5, 0.6));
  }
  .title span { display: block; }
  .title-lead { font-size: 26px; font-weight: 500; letter-spacing: 1px; }
  .title-main { font-size: 62px; font-weight: 700; letter-spacing: 1px; }
  .title-sub { font-size: 32px; font-weight: 500; letter-spacing: 1px; }
  .cover-emblem { margin-top: 22px; width: 290px; height: 290px; }
  .authors {
    position: absolute; bottom: 30px; left: 0; right: 0;
    text-align: center;
    font-family: 'Cormorant Garamond', serif;
    font-weight: 600; font-size: 18px; letter-spacing: 1.5px;
    color: var(--gold);
  }
</style>
</head>
<body>
  <div class="canvas">
    <div class="cover-spread">
      <div class="back-cover"></div>
      <div class="front-cover">
        <h1 class="title">
          <span class="title-lead">GUARDING</span>
          <span class="title-main">VIRGINIA</span>
          <span class="title-sub">THEFT</span>
          <span class="title-sub">CHARGES</span>
        </h1>
        <svg class="cover-emblem" viewBox="0 0 290 290">
          <defs>
            <linearGradient id="sceneFill" x1="0" y1="0" x2="0" y2="1">
              <stop offset="0" stop-color="var(--scene-sky)"/>
              <stop offset="0.45" stop-color="var(--scene-house)"/>
              <stop offset="1" stop-color="var(--scene-green)"/>
            </linearGradient>
          </defs>
          <circle cx="145" cy="145" r="142" fill="var(--ring)" stroke="var(--ring-edge)" stroke-width="2"/>
          <circle cx="145" cy="145" r="126" fill="url(#sceneFill)" role="img"
                  aria-label="Victorian house seen through a cracked pane of glass"/>
          <circle cx="145" cy="145" r="126" fill="none" stroke="var(--ring-edge)" stroke-width="1.5"/>
        </svg>
        <p class="authors">Owen T. Marsh and Philip R. Oakes</p>
      </div>
    </div>
  </div>
</body>
</html>
```